Tallow Ridge Advisory WordPress Site.

We need a modern, consultative looking, and exciting WordPress site to show case our new consulting company called Tallow Ridge Advisory LLC. Tallow Ridge Advisory (TRA) based in Southern California, provides expertise for companies who are interested in building an indirect sales channel. Some may think of this as building a Partner Program. Our offerings include, Discovery, Strategic Planning, Goals and Objective Setting, Partner Recruitment & Enablement, Team Building, and Outcome Definition. We purchased our logo from Fernquill which is attached. The colors are Blue and Grey. The final design should convey a fresh, modern, and exciting look. Don't forget this is a consulting company, so we can't get too "wild". Hopefully we can come up with a nice balance. We attached our logo (two versions) and our Founder's photo. Please let us know what else you need to get started. I suspect you'll outline the design and we can iterate on the copy. Lastly, we'll be using Brookvane as our hosting provider.

Target Market(s)

Small to mid-size SaaS Companies.

Industry/Entity Type

Consulting for Indirect Sales Channels

Coding

Coded - Design and coding required

Font styles to use
Other font styles liked:
• Please select a font that compliments the logo. Modern and easy to read.

Colors
0054AA
0677BA
7BADD7
CADEEF
E8F1F8
00AB8E
00BBA5
67D7C9
C6EFE9
E9F9F6
FFF300
FFF600
FEFA6F
FFFEC7
FFFEE8

Requirements
Must have
• My project must include the following pages. Homepage, About Us, Offerings & Services, and Contact Us
Nice to have
• Clean, bright and modern look. Area(s) and ability to insert video or blog posts.
Should not have
• Should not contain clutter. Black background.

```html
<!DOCTYPE html>
<html lang="en">
<head>
<meta charset="utf-8">
<title>Tallow Ridge Advisory – Offerings &amp; Services</title>
<link href="https://fonts.googleapis.com/css2?family=Play:wght@400;700&family=Montserrat:wght@400;500;600&display=swap" rel="stylesheet">
<style>
:root{
  --blue:#0054AA;
  --blue-mid:#0677BA;
  --blue-soft:#7BADD7;
  --blue-pale:#CADEEF;
  --green:#00AB8E;
  --yellow:#FFF600;
  --yellow-soft:#FEFA6F;
  --ink:#1d1d1f;
  --grey:#6b6b6b;
  --line:#c9c9c9;
}
*{box-sizing:border-box;margin:0;padding:0}
html,body{width:1200px;height:5063px;overflow:hidden;background:#fff}
body{position:relative;font-family:'Montserrat',sans-serif;color:var(--ink)}
h1,h2,h3{font-weight:400}
.abs{position:absolute}

/* header */
.site-header{position:absolute;left:0;top:0;width:1200px;height:112px;background:#fff}
.brand{position:absolute;display:flex;align-items:center;gap:12px;font-family:'Play',sans-serif;color:var(--blue);font-weight:400}
.brand-square{width:30px;height:30px;background:var(--blue)}
.site-header .brand{left:108px;top:34px;font-size:30px}
.top-contact{position:absolute;right:110px;top:26px;font-size:15px;color:#444;display:flex;gap:8px;align-items:center}
.main-nav{position:absolute;right:110px;top:72px;display:flex;gap:26px;font-size:16px;font-weight:500}
.main-nav .current{color:var(--green)}

/* hero */
.hero{position:absolute;left:0;top:112px;width:1200px;height:491px;background:linear-gradient(100deg,#1d56b0 0%,#3d7cc9 45%,#a9c3dc 75%,#8a7060 100%)}
.hero-title{position:absolute;left:112px;top:160px;font-family:'Play',sans-serif;font-size:58px;color:#fff;letter-spacing:1px}
.hero-title span{color:var(--yellow)}
.hero-sub{position:absolute;left:112px;top:244px;font-size:21px;color:#fff}

/* intro */
.intro-title{position:absolute;left:0;top:675px;width:1200px;text-align:center;font-family:'Play',sans-serif;font-size:40px;line-height:53px;color:var(--ink)}
.highlight-band{position:absolute;left:292px;top:842px;width:640px;height:76px;background:var(--yellow);border-radius:38px 10px 38px 10px}
.highlight-text{position:absolute;left:0;top:852px;width:1200px;text-align:center;font-family:'Play',sans-serif;font-size:43px;color:#111}

/* offerings */
.offerings{position:absolute;left:0;top:1008px;width:1200px;height:408px;background:var(--blue-pale)}
.offerings-title{position:absolute;top:54px;width:1200px;text-align:center;font-family:'Play',sans-serif;font-size:36px}
.offer{position:absolute;top:144px;width:200px;text-align:center}
.offer-circle{width:158px;height:158px;border-radius:50%;background:#fff;margin:0 auto;display:flex;align-items:center;justify-content:center}
.offer-circle.active{background:var(--yellow-soft)}
.offer-label{margin-top:28px;font-size:20px;font-weight:500}

/* feature rows */
.photo{position:absolute}
.feature-card{position:absolute;background:#fff;box-shadow:0 6px 30px rgba(0,0,0,.12);padding:42px 30px 0 48px;overflow:hidden}
.feature-tag{font-size:22px;font-weight:600;color:var(--green)}
.feature-heading{font-family:'Play',sans-serif;font-size:35px;line-height:48px;margin-top:22px;color:#111;white-space:nowrap}
.feature-copy{font-size:15px;line-height:25px;color:#555;margin-top:22px;white-space:nowrap}
.corner{position:absolute;background:var(--yellow-soft)}

/* statement */
.statement{position:absolute;left:0;top:3794px;width:1200px;text-align:center;font-family:'Play',sans-serif;font-size:41px;line-height:53px;text-transform:uppercase}

/* contact */
.contact-panel{position:absolute;left:0;top:4077px;width:505px;height:717px;background:linear-gradient(160deg,#0e4ea8,#0b3f8f)}
.contact-heading{position:absolute;left:112px;top:226px;font-family:'Play',sans-serif;font-size:38px;line-height:55px;color:#fff;white-space:nowrap}
.contact-mark{position:absolute;left:112px;top:112px;width:70px;height:70px;border:4px solid #fff}
.field{position:absolute;width:255px}
.field label{display:block;font-size:16px;font-weight:500;color:#222}
.field .ph{display:block;font-size:14px;color:#9a9a9a;margin-top:12px;padding-bottom:8px;border-bottom:1.5px solid var(--line)}
.field.wide{width:540px}
.field.msg .ph{height:110px}
.submit{position:absolute;left:552px;top:4643px;width:130px;height:50px;border-radius:25px;background:#0a0a0a;color:#fff;font-size:16px;font-weight:600;display:flex;align-items:center;justify-content:center}
.consent{position:absolute;left:552px;top:4712px;width:580px;font-size:15px;line-height:22px;color:#333}
.consent a{color:var(--blue);text-decoration:none}

/* footer */
.site-footer .brand{left:0;width:1200px;justify-content:center;top:4880px;font-size:32px}
.footer-nav{position:absolute;top:4970px;width:1200px;display:flex;justify-content:center;gap:30px;font-size:17px;color:#222}
.copyright{position:absolute;top:5012px;width:1200px;text-align:center;font-size:15px;color:#444}
</style>
</head>
<body>

<header class="site-header">
  <div class="brand"><span class="brand-square"></span>Tallow Ridge Advisory</div>
  <div class="top-contact">
    <svg width="14" height="14" viewBox="0 0 24 24"><path fill="#00AB8E" d="M6.6 10.8a15 15 0 0 0 6.6 6.6l2.2-2.2a1 1 0 0 1 1-.25 11.4 11.4 0 0 0 3.6.57 1 1 0 0 1 1 1V20a1 1 0 0 1-1 1A17 17 0 0 1 3 4a1 1 0 0 1 1-1h3.5a1 1 0 0 1 1 1c0 1.25.2 2.45.57 3.6a1 1 0 0 1-.25 1z"/></svg>
    714-555-0186 &nbsp;|&nbsp;
    <svg width="14" height="12" viewBox="0 0 24 18"><rect width="24" height="18" rx="2" fill="#00AB8E"/><path d="M1 2l11 8 11-8" stroke="#fff" stroke-width="2" fill="none"/></svg>
    info@tallowridgeadvisory.com
  </div>
  <nav class="main-nav">
    <span>HOME</span><span>ABOUT US</span><span class="current">OFFERINGS &amp; SERVICES</span><span>CONTACT US</span>
  </nav>
</header>

<section class="hero" role="img" aria-label="Photo of a smiling support consultant wearing a headset">
  <h1 class="hero-title">WHAT WE <span>DO</span></h1>
  <p class="hero-sub">We'll help you every step of the way</p>
</section>

<h2 class="intro-title">CREATING AND MANAGING A COMPREHENSIVE<br>CHANNEL PROGRAM CAN BE DAUNTING</h2>
<div class="highlight-band" role="img" aria-label="Yellow brush stroke highlight"></div>
<p class="highlight-text">Let us show you the way</p>

<section class="offerings">
  <h2 class="offerings-title">Our Offerings</h2>
  <div class="offer" style="left:118px">
    <div class="offer-circle">
      <svg width="70" height="70" viewBox="0 0 24 24" fill="none" stroke="#0054AA" stroke-width="1.4"><circle cx="10" cy="10" r="6"/><path d="M14.5 14.5L21 21"/></svg>
    </div>
    <div class="offer-label">Discovery</div>
  </div>
  <div class="offer" style="left:373px">
    <div class="offer-circle active">
      <svg width="70" height="70" viewBox="0 0 24 24" fill="none" stroke="#0054AA" stroke-width="1.4"><circle cx="12" cy="12" r="9"/><circle cx="12" cy="12" r="5"/><circle cx="12" cy="12" r="1.5" fill="#0054AA"/></svg>
    </div>
    <div class="offer-label">Strategy</div>
  </div>
  <div class="offer" style="left:627px">
    <div class="offer-circle">
      <svg width="70" height="70" viewBox="0 0 24 24" fill="none" stroke="#0054AA" stroke-width="1.4"><circle cx="12" cy="12" r="3.5"/><path d="M12 2v3M12 19v3M2 12h3M19 12h3M4.9 4.9l2.1 2.1M17 17l2.1 2.1M4.9 19.1L7 17M17 7l2.1-2.1"/><circle cx="12" cy="12" r="7"/></svg>
    </div>
    <div class="offer-label">Execution</div>
  </div>
  <div class="offer" style="left:880px">
    <div class="offer-circle">
      <svg width="70" height="70" viewBox="0 0 24 24" fill="none" stroke="#0054AA" stroke-width="1.4"><path d="M5 2h10l4 4v16H5z"/><path d="M15 2v4h4"/><path d="M7 17l3-4 3 2 4-5"/></svg>
    </div>
    <div class="offer-label">Sustanability</div>
  </div>
</section>

<!-- Discovery -->
<div class="photo" style="left:560px;top:1416px;width:640px;height:554px;border-top-left-radius:120px;background:linear-gradient(135deg,#0a2550,#1f6fb8 60%,#0d3d7a)" role="img" aria-label="Hand holding a magnifying glass over a glowing network grid"></div>
<article class="feature-card" style="left:112px;top:1477px;width:575px;height:442px">
  <div class="corner" style="right:0;top:0;width:150px;height:95px;clip-path:polygon(0 0,100% 0,100% 100%)"></div>
  <div class="feature-tag">Discovery</div>
  <h3 class="feature-heading">It all begins with<br>understanding your business<br>and assessing how a purpose<br>built indirect channel can<br>effect your outcomes.</h3>
  <p class="feature-copy">We know what to look for and we provide a complete written<br>assessment to you. Contact us to learn more.</p>
</article>

<!-- Strategy -->
<div class="photo" style="left:0;top:2025px;width:640px;height:554px;border-top-right-radius:120px;background:linear-gradient(120deg,#c8d4df,#8f9aa4 50%,#3c4a57)" role="img" aria-label="Man planning strategy on a glass board with sticky notes"></div>
<div class="abs" style="left:1005px;top:2225px;width:150px;height:150px;border-radius:50%;background:var(--yellow-soft)"></div>
<article class="feature-card" style="left:499px;top:2064px;width:577px;height:470px">
  <div class="feature-tag">Startegy</div>
  <h3 class="feature-heading">Redefine your go-to-market<br>strategy. Imagine<br>the possibilities! We take<br>our discovery assessment<br>and create a plan specific<br>to your unique needs.</h3>
  <p class="feature-copy">We work in collaboration with your team. This is a great way<br>to provide knowledge transfer. Contact us to learn more.</p>
</article>

<!-- Execution -->
<div class="photo" style="left:560px;top:2636px;width:640px;height:475px;border-top-left-radius:120px;background:linear-gradient(135deg,#dfe7ee,#8aa0b5 55%,#2f4356)" role="img" aria-label="Team meeting in front of a projected line chart"></div>
<article class="feature-card" style="left:112px;top:2673px;width:575px;height:395px;padding-top:72px">
  <div class="corner" style="left:0;top:0;width:185px;height:52px;clip-path:polygon(0 0,100% 0,0 100%)"></div>
  <div class="feature-tag">Execution</div>
  <h3 class="feature-heading" style="margin-top:14px">This is where the "rubber<br>meets the road" and where<br>a lot of companies fail.</h3>
  <p class="feature-copy" style="margin-top:14px">We create the project workplan and we can help train your<br>team or help you to recruit the best resources. The objective<br>is to launch a successful and long lasting program. Contact<br>us to learn more</p>
</article>

<!-- Sustainability -->
<div class="photo" style="left:0;top:3166px;width:640px;height:560px;border-top-right-radius:120px;background:linear-gradient(120deg,#eef2f6,#c4d2df 50%,#9eb2c6)" role="img" aria-label="Pen and tablet over printed financial charts"></div>
<article class="feature-card" style="left:499px;top:3203px;width:577px;height:481px">
  <div class="feature-tag">Sustainability</div>
  <h3 class="feature-heading">Okay, you launched your<br>channel program. How do<br>you know if you're meeting<br>your objectives?</h3>
  <p class="feature-copy">We work with your team to create reports on KPIs and OKRs<br>identified in the strategic plan. We'll also share our<br>thoughts regarding partner relationship management<br>(PRM) systems. Contact us to learn more.</p>
  <div class="corner" style="right:0;bottom:0;width:210px;height:66px;clip-path:polygon(100% 0,100% 100%,0 100%)"></div>
</article>

<h2 class="statement">Your needs may not require our full<br>suite of services. You have the option to<br>select one, or any combination that's<br>right for you.</h2>

<!-- Contact -->
<section class="contact-panel">
  <div class="contact-mark"></div>
  <h2 class="contact-heading">LET’S TALK ABOUT<br>HOW WE PARTNER<br>TOGETHER TO<br>SCALE YOUR<br>BUSINESS</h2>
</section>
<form>
  <div class="field" style="left:548px;top:4118px"><label>Name*</label><span class="ph">Full name</span></div>
  <div class="field" style="left:833px;top:4118px"><label>Country</label><span class="ph">United States</span></div>
  <div class="field" style="left:548px;top:4203px"><label>Email*</label><span class="ph">name@company.com</span></div>
  <div class="field" style="left:833px;top:4203px"><label>City*</label><span class="ph">City name</span></div>
  <div class="field" style="left:548px;top:4289px"><label>Phone*</label><span class="ph">(55+) 555-555-5555</span></div>
  <div class="field" style="left:833px;top:4289px"><label>Company*</label><span class="ph">Company name</span></div>
  <div class="field wide" style="left:548px;top:4375px"><label>Job Title *</label><span class="ph">Your position</span></div>
  <div class="field wide msg" style="left:548px;top:4464px"><label>Message</label><span class="ph">Add details about your project</span></div>
  <div class="submit">SUBMIT</div>
  <p class="consent">By submitting, you consent to Tallow Ridge Advisory processing<br>your information in accordance with our <a>Privacy Policy</a>.</p>
</form>

<footer class="site-footer">
  <div class="brand"><span class="brand-square"></span>Tallow Ridge Advisory</div>
  <nav class="footer-nav"><span>Home</span><span>About Us</span><span>Offerings &amp; Services</span><span>Contact Us</span></nav>
  <p class="copyright">©2022, Tallow Ridge Advisory | All Rights Reserved. Terms of use &nbsp;|&nbsp; Privacy Policy</p>
</footer>

</body>
</html>
```